Website Design for Spatial Humanities Non-Profit: Lantern Ridge Atlas

We seek a Wordpress website template for Lantern Ridge Atlas (LRA) a 501(c)(3) non-profit in the emergent field of spatial humanities dedicated to digitally preserving global historic and cultural sites. A unique collaboration between individuals in diverse disciplines (academia, technology, arts, and social entrepreneurship), LRA melds age-old scholarship with 21st Century technology to assert the importance of physical location to the understanding of history. This actualized focus allows for a more comprehensive, interactive, and “living” reconstruction of the past than previously thought possible.
LRA, through its own initiatives as well as those of others to whom it provides services, has created a prototype for digital preservation applicable to every country, culture, and subject matter. The organization is
• Pioneering new technology and multimedia techniques for documenting historic and cultural sites;
• Leading international field expeditions to geo-locate and digitize sites, as well as record eyewitness testimony; and
• Transforming research data into dynamically new educational applications.
The template should have a distinctive homepage, themed pages (about, news, projects, opportunities), and no blog elements (e.g., comment section). Admin friendliness is a plus.
We have posted separately for a logo design, which will perhaps feature a scattering of pixels horizontally that gradually cohere to form a globe (featuring "LRA") in the center. To participate in that contest see: http://work.briefmarket-example.com/task.aspx?id=40217
Non-Profit

```html
<!DOCTYPE html>
<html lang="en">
<head>
<meta charset="utf-8">
<title>Lantern Ridge Atlas</title>
<link rel="stylesheet" href="https://fonts.googleapis.com/css2?family=Merriweather:wght@300;400&family=Signika:wght@300;400&display=swap">
<style>
  :root {
    --band-olive: #9c9d7b;
    --band-olive-dark: #8d8e6d;
    --band-khaki: #d5d19d;
    --band-khaki-light: #dcd8a8;
    --rule-light: #e9e6c4;
    --ink: #2e2d22;
    --ink-soft: #4a4936;
    --button: #2f302b;
    --button-edge: #55564f;
    --footer: #121310;
    --footer-rule: #2a2b25;
    --footer-text: #e8e6dc;
    --bullet: #a9a47a;
    --heading-font: "Signika", "Trebuchet MS", sans-serif;
    --body-font: "Merriweather", Georgia, serif;
  }
  * { box-sizing: border-box; margin: 0; padding: 0; }
  html, body { width: 1200px; height: 1013px; overflow: hidden; }
  body { position: relative; font-family: var(--body-font); color: var(--ink); background: var(--footer); }

  .band-teasers {
    position: absolute; left: 0; top: 0; width: 1200px; height: 126px;
    background:
      repeating-linear-gradient(45deg, rgba(255,255,255,.05) 0 2px, transparent 2px 5px),
      repeating-linear-gradient(-45deg, rgba(0,0,0,.04) 0 2px, transparent 2px 5px),
      linear-gradient(var(--band-olive), var(--band-olive-dark));
    border-bottom: 2px solid var(--rule-light);
  }
  .teaser-thumb { position: absolute; top: 0; width: 126px; height: 32px; box-shadow: 0 2px 4px rgba(0,0,0,.45); }
  .teaser-thumb.sunset { left: 69px; background: linear-gradient(#6b3d12, #e38a1c 60%, #3a1d07); }
  .teaser-thumb.pier { left: 609px; background: linear-gradient(#9fb4cf, #c9d4e1 60%, #7c8aa0); }
  .teaser-text {
    position: absolute; top: -8px; width: 360px;
    font-size: 13.5px; line-height: 20px; letter-spacing: .3px; color: var(--ink);
  }
  .teaser-text.first { left: 224px; }
  .teaser-text.second { left: 764px; }

  .button {
    position: absolute; display: flex; align-items: center; justify-content: center;
    background: linear-gradient(#45463f, var(--button) 55%, #24251f);
    border: 1px solid var(--button-edge); border-radius: 2px;
    color: #f1efe6; font-family: var(--heading-font); font-size: 13px; letter-spacing: 1px;
    box-shadow: 0 1px 3px rgba(0,0,0,.4);
  }
  .teaser-button-1 { left: 460px; top: 62px; width: 123px; height: 25px; }
  .teaser-button-2 { left: 1001px; top: 62px; width: 123px; height: 25px; }

  .band-session {
    position: absolute; left: 0; top: 128px; width: 1200px; height: 552px;
    background:
      repeating-linear-gradient(45deg, rgba(255,255,255,.08) 0 2px, transparent 2px 5px),
      repeating-linear-gradient(-45deg, rgba(120,110,60,.06) 0 2px, transparent 2px 5px),
      linear-gradient(var(--band-khaki-light), var(--band-khaki));
    border-bottom: 2px solid var(--rule-light);
  }
  .session-title {
    position: absolute; left: 64px; top: 45px;
    font-family: var(--heading-font); font-weight: 300; font-size: 23px; letter-spacing: 1.2px; color: var(--ink-soft);
  }
  .session-intro {
    position: absolute; left: 64px; top: 88px; width: 272px;
    font-size: 14.5px; line-height: 20.3px; letter-spacing: .3px; color: var(--ink);
  }
  .session-button { left: 64px; top: 279px; width: 124px; height: 26px; font-family: var(--body-font); font-size: 14px; }

  .gallery-item { position: absolute; width: 338px; }
  .gallery-image { width: 338px; height: 169px; box-shadow: 1px 2px 4px rgba(0,0,0,.45); border: 1px solid rgba(255,255,255,.6); }
  .gallery-caption {
    margin: 12px 0 0 2px; width: 336px; padding-bottom: 8px;
    border-bottom: 1px solid #55543e;
    font-size: 14px; letter-spacing: 1px; color: var(--ink-soft);
  }
  .item-a { left: 402px; top: 53px; }
  .item-b { left: 784px; top: 53px; }
  .item-c { left: 402px; top: 306px; }
  .item-d { left: 784px; top: 306px; }
  .world-rose { background: radial-gradient(ellipse at 50% 45%, #f6c9b3, #eba58b 75%); }
  .harbour-bridge { background: linear-gradient(#3d7fd1, #cfe1f2 45%, #8a9aa8 70%, #4f5a5e); }
  .world-parchment { background: radial-gradient(ellipse at 50% 50%, #c3b18a, #9d8a60 80%); }
  .relief-blue { background: linear-gradient(100deg, #7d8184 0%, #c3c7c9 35%, #34b7dc 55%, #1ba4d1 100%); }

  .site-footer { position: absolute; left: 0; top: 680px; width: 1200px; height: 333px; background: var(--footer); color: var(--footer-text); }
  .footer-column { position: absolute; top: 32px; width: 220px; }
  .footer-column.pages { left: 69px; }
  .footer-column.updates { left: 339px; }
  .footer-column.contact { left: 610px; }
  .footer-column.affiliates { left: 881px; }
  .footer-divider { position: absolute; top: 32px; width: 1px; height: 195px; background: var(--footer-rule); }
  .footer-heading {
    font-family: var(--heading-font); font-weight: 400; font-size: 24px; line-height: 22px;
    letter-spacing: .5px; height: 44px;
  }
  .page-links { list-style: none; width: 173px; border-top: 1px solid var(--footer-rule); margin-top: -3px; }
  .page-links li { height: 30.5px; line-height: 29px; border-bottom: 1px solid var(--footer-rule); font-size: 16px; letter-spacing: .3px; }
  .arrow-list { list-style: none; font-size: 14.5px; line-height: 22.5px; }
  .arrow-list li { position: relative; padding-left: 18px; }
  .arrow-list li::before {
    content: ""; position: absolute; left: 2px; top: 7px; width: 5px; height: 5px;
    border-top: 2px solid var(--bullet); border-right: 2px solid var(--bullet); transform: rotate(45deg);
  }
  .updates .arrow-list li { margin-bottom: 10px; width: 150px; }
  .affiliates .arrow-list { width: 170px; }
  .contact-details { padding-left: 13px; font-size: 14.5px; line-height: 22.5px; }
  .brand-sign { position: absolute; right: 74px; top: 262px; text-align: right; }
  .brand-name { font-family: var(--heading-font); font-weight: 300; font-size: 30px; letter-spacing: 1px; line-height: 34px; }
  .brand-note { font-size: 14px; line-height: 18px; }
</style>
</head>
<body>
  <section class="band-teasers">
    <div class="teaser-thumb sunset" role="img" aria-label="Sunset photograph over a landscape"></div>
    <p class="teaser-text first">lum ipsum odio, faucibus a semper eget, ultrices a velit. Proin a lorem et justo pellentesque pellen-</p>
    <div class="button teaser-button-1">read more</div>
    <div class="teaser-thumb pier" role="img" aria-label="Photograph of a wooden pier over water"></div>
    <p class="teaser-text second">lum ipsum odio, faucibus a semper eget, ultrices a velit. Proin a lorem et justo pellentesque pellen-</p>
    <div class="button teaser-button-2">read more</div>
  </section>

  <section class="band-session">
    <h2 class="session-title">Title of the session</h2>
    <p class="session-intro">Sed semper sagittis ligula, ac con-vallis dolor lobortis vel. Aenean lacinia, sem non volutpat fermen-tum, sem enim venenatis turpis, vitae dapibus sem erat vehicula dolor. Donec eget felis ut lacus adipiscing sodales eget mattis lacus.</p>
    <div class="button session-button">read more</div>

    <figure class="gallery-item item-a">
      <div class="gallery-image world-rose" role="img" aria-label="Glowing world map on a rose background"></div>
      <figcaption class="gallery-caption">Description Image</figcaption>
    </figure>
    <figure class="gallery-item item-b">
      <div class="gallery-image harbour-bridge" role="img" aria-label="Harbour with cranes and a cable-stayed bridge under a cloudy sky"></div>
      <figcaption class="gallery-caption">Description Image</figcaption>
    </figure>
    <figure class="gallery-item item-c">
      <div class="gallery-image world-parchment" role="img" aria-label="World map on aged parchment"></div>
      <figcaption class="gallery-caption">Description Image</figcaption>
    </figure>
    <figure class="gallery-item item-d">
      <div class="gallery-image relief-blue" role="img" aria-label="Blue relief map of a coastline on grey"></div>
      <figcaption class="gallery-caption">Description Image</figcaption>
    </figure>
  </section>

  <footer class="site-footer">
    <div class="footer-column pages">
      <h3 class="footer-heading">Pages</h3>
      <ul class="page-links">
        <li>Home Page</li><li>About us</li><li>Technology</li><li>Research</li><li>Contact</li>
      </ul>
    </div>
    <div class="footer-divider" style="left:285px"></div>
    <div class="footer-column updates">
      <h3 class="footer-heading">Last updates</h3>
      <ul class="arrow-list">
        <li>In hac habitasse platea dictumst. Praesent iaculis</li>
        <li>Faucibus pretium. Nullam dictum viverra augue id</li>
      </ul>
    </div>
    <div class="footer-divider" style="left:553px"></div>
    <div class="footer-column contact">
      <h3 class="footer-heading">Contact<br>information</h3>
      <p class="contact-details">Our telephones:<br>150440736<br>164220519<br>Our email:<br>hello@lanternridge-example.org</p>
    </div>
    <div class="footer-divider" style="left:823px"></div>
    <div class="footer-column affiliates">
      <h3 class="footer-heading">Our affiliates</h3>
      <ul class="arrow-list">
        <li>Lorem ipsum dolor</li><li>Egestas diam</li><li>Aliquet Hendrerit</li>
        <li>Libero et sudis</li><li>Non potest augue</li><li>Vehicula tempus porta</li>
      </ul>
    </div>
    <div class="brand-sign">
      <div class="brand-name">Lantern Ridge Atlas</div>
      <div class="brand-note">all rights reserved.</div>
    </div>
  </footer>
</body>
</html>
```